Quorvel Landing page redesign

We are looking for a landing page redesign before we officially launch. We want to incorporate the information already on the site at www.Quorvel.example landing page but make it more inviting. There needs to be a sign up section along with clearly stating what we do. Having a place for sample profiles and linking to our blog and podcast is option. More information about all we will be doing is at Quorvel is on the landing page and also on the blog.

Target Market(s)

35 years old and up.

Coding

Coded - Design and coding required

Number of Pages Required

1 page

Requirements
Must have
• The top bar and the bottom bar (with the privacy policy, etc)
• Sign in/up section.
• I don't want to give to much here because I want designers to be creative.
Nice to have
• Prefer not to have a landing page that requires a lot of scrolling at all.

```html
<!DOCTYPE html>
<html lang="en">
<head>
<meta charset="utf-8">
<title>Quorvel</title>
<link href="https://fonts.googleapis.com/css2?family=Ubuntu:wght@300;400;500;700&display=swap" rel="stylesheet">
<style>
:root{
  --navy:#1c2a7a;
  --ink:#1d1f2e;
  --accent:#d63a17;
  --band:#f6f6f6;
  --line:#e1e1e1;
  --white:#ffffff;
  --muted:#4a4a55;
}
*{box-sizing:border-box;margin:0;padding:0}
html,body{width:1200px;height:1112px;overflow:hidden;background:var(--white)}
body{font-family:"Ubuntu",sans-serif;color:var(--ink);position:relative}
.site-header{position:absolute;left:0;top:0;width:1200px;height:86px}
.brand{position:absolute;display:flex;align-items:center;height:30px}
.brand-name{font-family:"Ubuntu",sans-serif;font-weight:400;font-size:23px;color:var(--ink);letter-spacing:.2px}
.site-header .brand{left:136px;top:28px}
.main-nav{position:absolute;top:25px;left:688px;display:flex;align-items:center;height:36px}
.nav-link{font-weight:500;font-size:14px;color:var(--ink);text-decoration:none;position:relative;height:36px;line-height:36px}
.nav-link.active::after{content:"";position:absolute;left:-7px;right:-7px;bottom:-1px;height:3px;background:var(--ink)}
.nav-blog{margin-left:7px}
.nav-pod{margin-left:34px}
.btn-login{margin-left:24px;width:99px;height:35px;background:var(--accent);color:var(--white);border-radius:3px;display:flex;align-items:center;justify-content:center;gap:8px;font-weight:500;font-size:14px;text-decoration:none}
.nav-privacy{margin-left:19px;font-size:9.5px;font-weight:500;color:var(--ink);text-decoration:none}
.hero{position:absolute;left:0;top:86px;width:1200px;height:492px;background:radial-gradient(ellipse at 55% 45%,#4a4a6e 0%,#2f3152 45%,#1e2038 100%);color:var(--white);text-align:center}
.hero-title{position:absolute;top:139px;width:100%;font-weight:500;font-size:24px}
.field{position:absolute;left:404px;width:387px;height:45px;border:1px solid rgba(255,255,255,.9);border-radius:3px;background:rgba(20,20,40,.35);color:var(--white);font-size:11.5px;font-weight:300;padding:0 14px;text-align:left;display:flex;align-items:center}
.field-name{top:198px}
.field-email{top:261px}
.btn-signup{position:absolute;left:519px;top:335px;width:162px;height:40px;background:var(--accent);border-radius:3px;font-weight:500;font-size:19px;line-height:40px;color:var(--white)}
.hero-note{position:absolute;top:399px;width:100%;font-size:14px;font-weight:500}
.dots{position:absolute;top:457px;left:564px;display:flex;gap:14px}
.dot{width:7px;height:7px;border-radius:50%;background:var(--white)}
.dot.current{background:var(--accent)}
.features{position:absolute;left:0;top:578px;width:1200px;height:117px;background:var(--band)}
.feature{position:absolute;top:48px;display:flex;align-items:center;gap:12px;font-size:12.5px;font-weight:300;line-height:14.5px;color:var(--muted)}
.feature svg{flex:none}
.section-title{position:absolute;top:748px;width:100%;text-align:center;font-weight:500;font-size:24px;color:var(--accent)}
.profile-card{position:absolute;top:816px;width:288px;height:140px;border:1px solid var(--line);background:var(--white)}
.profile-photo{position:absolute;left:16px;top:18px;width:108px;height:102px}
.profile-body{position:absolute;left:135px;top:16px;width:136px}
.profile-name{font-weight:700;font-size:12.5px;color:var(--navy)}
.profile-aka{margin-top:8px;font-size:12px;font-weight:300;color:var(--ink)}
.profile-text{margin-top:7px;font-size:8.6px;font-weight:300;line-height:14px;color:var(--muted)}
.btn-view{display:inline-block;margin-top:8px;background:var(--accent);color:var(--white);font-size:8.5px;font-weight:700;padding:4px 6px;text-decoration:none}
.site-footer{position:absolute;left:0;top:1015px;width:1200px;height:97px;background:var(--band)}
.site-footer .brand{left:136px;top:34px}
.footer-privacy{position:absolute;left:969px;top:48px;font-size:11px;color:var(--ink);text-decoration:none}
</style>
</head>
<body>
<header class="site-header">
  <div class="brand"><span class="brand-name">Quorvel</span></div>
  <nav class="main-nav">
    <a class="nav-link nav-blog active" href="#">BLOG</a>
    <a class="nav-link nav-pod" href="#">POD CAST</a>
    <a class="btn-login" href="#"><svg width="9" height="11" viewBox="0 0 9 11"><path d="M2 5V3.3a2.5 2.5 0 0 1 5 0V5" fill="none" stroke="#fff" stroke-width="1.5"/><rect x="0.5" y="5" width="8" height="6" rx="1" fill="#fff"/></svg>LOGIN</a>
    <a class="nav-privacy" href="#">PRIVACY POLICY</a>
  </nav>
</header>

<section class="hero" role="img" aria-label="Family reading a book together on a sofa, dimmed navy overlay">
  <h1 class="hero-title">Sign Up Now</h1>
  <div class="field field-name">Enter Your Name</div>
  <div class="field field-email">Enter Your E-mail</div>
  <div class="btn-signup">SIGN UP</div>
  <p class="hero-note">Already Have an Account? Sign Up</p>
  <div class="dots"><span class="dot current"></span><span class="dot"></span><span class="dot"></span><span class="dot"></span></div>
</section>

<section class="features">
  <div class="feature" style="left:146px">
    <svg width="26" height="26" viewBox="0 0 26 26"><path d="M3 23l1.5-6L17 4.5l4.5 4.5L9 21.5z" fill="var(--navy)"/><path d="M18.5 3l2-2 4.5 4.5-2 2z" fill="var(--navy)"/><path d="M5.5 17.5l3 3" stroke="#fff" stroke-width="1.2"/></svg>
    <span>Create Timelines,<br>Maps, Family Trees</span>
  </div>
  <div class="feature" style="left:341px">
    <svg width="30" height="27" viewBox="0 0 30 27"><path d="M15 26L3 14A7.5 7.5 0 0 1 15 4a7.5 7.5 0 0 1 12 10z" fill="var(--navy)"/></svg>
    <span>Memorialize<br>Loved Ones</span>
  </div>
  <div class="feature" style="left:508px">
    <svg width="27" height="27" viewBox="0 0 27 27"><path d="M7 1h18l-5 21H2z" fill="var(--navy)"/><path d="M2 22h18l-1 4H3a2 2 0 0 1-1-4z" fill="none" stroke="var(--navy)" stroke-width="2"/><path d="M9 7h10M8 11h10" stroke="#fff" stroke-width="1.5"/></svg>
    <span>Share Family Stories,<br>History and more</span>
  </div>
  <div class="feature" style="left:705px">
    <svg width="31" height="20" viewBox="0 0 31 20"><rect x="0" y="1" width="31" height="18" rx="9" fill="var(--navy)"/><path d="M6 10h7M9.5 6.5v7" stroke="#fff" stroke-width="2.2"/><circle cx="21" cy="8" r="2" fill="#fff"/><circle cx="25" cy="12" r="2" fill="#fff"/></svg>
    <span>Control Your<br>Privacy</span>
  </div>
  <div class="feature" style="left:857px">
    <svg width="30" height="26" viewBox="0 0 30 26"><ellipse cx="12" cy="10" rx="10.5" ry="8" fill="none" stroke="var(--navy)" stroke-width="2.2"/><path d="M5 16l-3 6 7-3" fill="var(--navy)"/><path d="M22 8a9 7.5 0 0 1 3 13l2 4-6-2.5a10 8 0 0 1-8-2" fill="none" stroke="var(--navy)" stroke-width="2.2"/></svg>
    <span>No Ads, No Like Buttons<br>No News Feeds</span>
  </div>
</section>

<h2 class="section-title">SAMPLE QUORVEL PROFILES</h2>

<article class="profile-card" style="left:144px">
  <div class="profile-photo" role="img" aria-label="Portrait of a smiling man in a denim shirt outdoors" style="background:linear-gradient(135deg,#7d9b6a,#4d6f9e 60%,#8ca9cc)"></div>
  <div class="profile-body">
    <h3 class="profile-name">Martin Ellory</h3>
    <p class="profile-aka">Aka : Sam</p>
    <p class="profile-text">Sed ut perspiciatis unde omnis<br>iste natus error sit vol</p>
    <a class="btn-view" href="#">VIEW PROFILE</a>
  </div>
</article>
<article class="profile-card" style="left:456px">
  <div class="profile-photo" role="img" aria-label="Portrait of a bearded man with glasses against a brick wall" style="background:linear-gradient(135deg,#9b5a46,#3b3c4c 55%,#a06650)"></div>
  <div class="profile-body">
    <h3 class="profile-name">Martin Ellory</h3>
    <p class="profile-aka">Aka : Sam</p>
    <p class="profile-text">Sed ut perspiciatis unde omnis<br>iste natus error sit vol</p>
    <a class="btn-view" href="#">VIEW PROFILE</a>
  </div>
</article>
<article class="profile-card" style="left:769px">
  <div class="profile-photo" role="img" aria-label="Portrait of a grinning middle-aged man in a garden" style="background:linear-gradient(135deg,#4c6b2c,#8a7560 55%,#3e5526)"></div>
  <div class="profile-body">
    <h3 class="profile-name">Martin Ellory</h3>
    <p class="profile-aka">Aka : Sam</p>
    <p class="profile-text">Sed ut perspiciatis unde omnis<br>iste natus error sit vol</p>
    <a class="btn-view" href="#">VIEW PROFILE</a>
  </div>
</article>

<footer class="site-footer">
  <div class="brand"><span class="brand-name">Quorvel</span></div>
  <a class="footer-privacy" href="#">PRIVACY POLICY</a>
</footer>
</body>
</html>
```